I need a simple, classy and stylish business card. I would like it to have a black background with white writing. I would like you to use my logo you designed on the front with the word 'Imagery" used underneath it in the same font. On the back I was thinking of the website at the top 'tomverrick.com' Then my social media accounts, Can you use the instagram, Facebook and twitter logo then my handles?
Please let me know what you think.
Regards Tom
Must have
- Website: www.tomverrick.com
- Social media handles..
- Instagram: @Tom_Verrick_Imagery
- Facebook: Tom Verrick Imagery
- Twitter: @Tom_Verrick
- Email: info@tomverick.com
- Phone: 0437 518 293

```html
<!DOCTYPE html>
<html lang="en">
<head>
<meta charset="utf-8">
<title>Tom Verrick Imagery – Business Card</title>
<link rel="stylesheet" href="https://fonts.googleapis.com/css2?family=Josefin+Sans:wght@300;400&display=swap">
<style>
  :root {
    --backdrop: #2b2927;
    --card: #0d0d0d;
    --ink: #f2f2f2;
    --ink-soft: #d9d9d9;
  }
  * { box-sizing: border-box; margin: 0; padding: 0; }
  html, body {
    width: 1200px; height: 727px; overflow: hidden;
    background: var(--backdrop);
    font-family: "Josefin Sans", sans-serif;
    color: var(--ink);
  }
  .stage {
    position: relative; width: 1200px; height: 727px;
    display: flex; align-items: center; justify-content: center; gap: 40px;
  }
  .card {
    position: relative; width: 530px; height: 305px;
    background: var(--card);
    box-shadow: 0 10px 30px rgba(0,0,0,.45);
    overflow: hidden;
  }

  /* Back side */
  .card-back .rule-top {
    position: absolute; left: 30px; right: 30px; top: 34px;
    height: 1px; background: var(--ink);
  }
  .card-back .site-row {
    position: absolute; left: 30px; right: 30px; top: 52px;
    display: flex; align-items: center; gap: 14px;
    font-size: 15px; font-weight: 300; letter-spacing: .6px;
  }
  .site-row .rule { flex: 1; height: 1px; background: var(--ink); }
  .card-back .socials {
    position: absolute; left: 30px; right: 30px; top: 86px;
    display: flex; justify-content: space-between; align-items: center;
    font-size: 12.5px; font-weight: 300; letter-spacing: .3px;
  }
  .handle { display: flex; align-items: center; gap: 6px; white-space: nowrap; }
  .handle .mark { width: 10px; height: 10px; background: var(--ink); border-radius: 2px; }
  .card-back .rule-bottom {
    position: absolute; left: 30px; right: 30px; top: 114px;
    height: 1px; background: var(--ink);
  }
  .card-back .brand {
    position: absolute; left: 40px; bottom: 70px;
  }

  /* Shared brand */
  .brand { display: flex; align-items: center; gap: 12px; }
  .brand .dot {
    width: 22px; height: 22px; border: 1.5px solid var(--ink); border-radius: 50%;
  }
  .brand .name {
    font-size: 30px; font-weight: 300; letter-spacing: 1.5px; white-space: nowrap;
  }

  /* Front side */
  .card-front .brand {
    position: absolute; left: 150px; top: 132px;
  }
  .card-front .brand .name { font-size: 27px; }
  .card-front .divider {
    position: absolute; left: 368px; top: 105px;
    width: 1px; height: 95px; background: var(--ink-soft);
  }
  .card-front .contact {
    position: absolute; left: 386px; top: 128px;
    display: flex; flex-direction: column; gap: 12px;
    font-size: 15px; font-weight: 300; letter-spacing: .6px;
  }
  .contact .line { display: flex; align-items: center; gap: 7px; white-space: nowrap; }
  .contact svg { width: 15px; height: 13px; fill: var(--ink); flex: none; }
  .contact .email { font-size: 13px; }
</style>
</head>
<body>
<main class="stage">
  <section class="card card-back" aria-label="Card back">
    <div class="rule-top"></div>
    <div class="site-row">
      <span class="rule"></span>
      <span class="site">www.tomverrick.com</span>
      <span class="rule"></span>
    </div>
    <div class="socials">
      <span class="handle"><span class="mark"></span>@Tom_Verrick_Imagery</span>
      <span class="handle"><span class="mark"></span>@TomVerrickImagery</span>
      <span class="handle"><span class="mark"></span>@Tom_Verrick</span>
    </div>
    <div class="rule-bottom"></div>
    <div class="brand">
      <span class="dot"></span>
      <span class="name">Tom Verrick</span>
    </div>
  </section>

  <section class="card card-front" aria-label="Card front">
    <div class="brand">
      <span class="dot"></span>
      <span class="name">Tom Verrick</span>
    </div>
    <div class="divider"></div>
    <div class="contact">
      <div class="line">
        <svg viewBox="0 0 15 13" aria-hidden="true">
          <path d="M1 4 Q7.5 -1 14 4 L12.5 6 L10 5 L10 3.5 Q7.5 2.5 5 3.5 L5 5 L2.5 6 Z"/>
          <rect x="3" y="7" width="9" height="5" rx="1"/>
        </svg>
        <span>0437 518 293</span>
      </div>
      <div class="line email">
        <svg viewBox="0 0 15 13" aria-hidden="true">
          <path d="M1 2 H14 V11 H1 Z M2 3 V3.6 L7.5 7.5 L13 3.6 V3 Z" fill-rule="evenodd"/>
        </svg>
        <span>info@tomverick.com</span>
      </div>
    </div>
  </section>
</main>
</body>
</html>
```